Brochure Design Project for Building Designer

I need a modern and edgy brochure to introduce my new business TORV Design, Commercial and Residential Building Designers.

We specialise in Building Design, Project Management and Design Consultation.

I would like the brochure to be anywhere between 2-4 pages, depending of amount of suitable content available.
Colours to be black and white with splashes of
bright colours (mostly incorporated in photos).

Main Content of brochure to be broken up into 3 (maybe 4) sections to include:

About Us
Services
Projects

Logo Text (DESIGN etc) can be changed to white if suits better with black background.

Would be nice to include sketches to give it that architectural feel.

Samples and wording will be uploaded shortly
Updates

I HAVE PROVIDED A COMPLETE UPDATE OF PROJECT REQUIREMENTS INCLUDING ALL NEW UPLOADED FILES.

PLEASE REFER TO THE BROCHURE LAYOUT PDF UPLOADEDĀ FOR FULL INFORMATION ON PROJECT INCLUDING BROCHURE LAYOUT.

IF YOU HAVE ANY QUESTIONS OR REQUIRE ANY FURTHER INFORMATION, PLEASE LET ME KNOW

I HAVE ADDED FURTHER DEVELOPED PDF DOCUMENTS OF BROCHURE.

IF YOU HAVE TROUBLE OPENING THESE DOCS IN ADOBE ILLUSTRATOR THRU ADOBE BRIDGE PLEASE LET ME KNOW & I WILL UPLOAD AI FILES.

CAN YOU PLEASE FINE TUNE GRAPHICS AND WORK ON BACKGROUND

Target Market(s)

Builders, Property Developers, Architects, Consultants, Professionals

Industry/Entity Type

Business

Requirements
Must have
• Very Professional Look
Black and White
Simple and easy to read layout
Either A4 (if only 2 pages) or
A3 double sided with centre fold (if 4 pages)
Touch up of photos (if possible) to make them stand out of the page.
Samples of recent projects with photos
Should not have
• Any comics or similar

```html
<!DOCTYPE html>
<html lang="en">
<head>
<meta charset="utf-8">
<title>TORV Design – Brochure Cover Spread</title>
<link rel="stylesheet" href="https://fonts.googleapis.com/css2?family=Open+Sans:wght@400;600&display=swap">
<style>
  :root {
    --ink: #231f20;
    --paper: #ffffff;
    --brand-pink: #e8378f;
    --text-dark: #2e2e2e;
    --text-light: #f2f2f2;
    --sketch-pale: #f4f4f4;
    --sketch-light: #e6e6e6;
    --sketch-mid: #cfcfcf;
    --sketch-deep: #b9b9b9;
  }
  * { box-sizing: border-box; margin: 0; padding: 0; }
  html, body {
    width: 1200px; height: 460px; overflow: hidden;
    background: var(--paper);
    font-family: "Open Sans", Arial, sans-serif;
  }
  .spread { display: flex; width: 1200px; height: 460px; }

  /* Back cover */
  .back-cover {
    position: relative; width: 600px; height: 460px;
    background: var(--ink); color: var(--text-light);
  }
  .back-cover__brand {
    position: absolute; left: 0; right: 0; top: 342px;
    text-align: center;
  }
  .back-cover__name {
    font-weight: 400; font-size: 44px; line-height: 1;
    letter-spacing: 3px; color: var(--brand-pink);
  }
  .back-cover__tagline {
    font-size: 5px; letter-spacing: 0.2px; margin-top: 3px;
    color: var(--text-light);
  }
  .back-cover__contact {
    position: absolute; left: 0; right: 0; top: 411px;
    text-align: center; font-size: 10.5px; line-height: 17px;
  }

  /* Front cover */
  .front-cover {
    position: relative; width: 600px; height: 460px;
    background: var(--paper); overflow: hidden;
  }
  .front-cover__sketch {
    position: absolute; left: 40px; top: 22px; width: 560px; height: 375px;
    background:
      linear-gradient(180deg, rgba(255,255,255,0) 0%, rgba(255,255,255,0) 72%, var(--paper) 100%),
      linear-gradient(90deg, var(--paper) 0%, rgba(255,255,255,0) 14%, rgba(255,255,255,0) 90%, var(--paper) 100%),
      linear-gradient(180deg, var(--paper) 0%, var(--sketch-pale) 12%, var(--sketch-light) 30%, var(--sketch-mid) 55%, var(--sketch-deep) 70%, var(--sketch-light) 86%, var(--sketch-pale) 100%);
  }
  .front-cover__brand { position: absolute; left: 156px; top: 100px; }
  .front-cover__name {
    font-weight: 400; font-size: 140px; line-height: 1;
    letter-spacing: 6px; color: var(--brand-pink);
  }
  .front-cover__tagline {
    font-size: 11px; letter-spacing: 0.3px; margin-top: 16px;
    color: var(--text-dark);
  }
  .front-cover__sectors {
    position: absolute; left: 18px; right: 14px; top: 426px;
    display: flex; justify-content: space-between;
    font-size: 16px; letter-spacing: 0.8px; color: var(--text-dark);
  }
</style>
</head>
<body>
<main class="spread">
  <section class="back-cover">
    <div class="back-cover__brand">
      <div class="back-cover__name">TORV</div>
      <div class="back-cover__tagline">COMMERCIAL + RESIDENTIAL BUILDING DESIGNERS</div>
    </div>
    <div class="back-cover__contact">
      <p>PO Box 482, Harlow Bay WA 6950 | Phone : 0491 570 112</p>
      <p>Email : yourname@torvdesign.com.au | Web : www.torvdesign.com.au</p>
    </div>
  </section>

  <section class="front-cover">
    <div class="front-cover__sketch" role="img" aria-label="Faint grey architectural line sketch of a multi-storey glazed commercial building in perspective"></div>
    <div class="front-cover__brand">
      <h1 class="front-cover__name">TORV</h1>
      <p class="front-cover__tagline">COMMERCIAL + RESIDENTIAL BUILDING DESIGNERS</p>
    </div>
    <p class="front-cover__sectors">
      <span>RESIDENTIAL</span><span>|</span><span>MULTI-UNIT RESIDENTIAL</span><span>|</span><span>COMMERCIAL</span><span>|</span><span>HEALTHCARE</span>
    </p>
  </section>
</main>
</body>
</html>
```